Bright Path Flyer Design for Virtual Online Clinic. -5.5 x 8.5 inches (half sheet)

We need a clean, modern flyer design for Bright Path, a new virtual walk-in clinic based in British Columbia. The flyer will be used in libraries, pharmacies, and community centers to help residents easily access primary care through their Bright Path NFC access card.
The flyer will ask a question : NEED A DOCTOR? This should be large and attention grabbing.
The design should clearly feature a Bright Path card image (the access card) as the centerpiece and visually show how patients can use it to book appointments. The tone should feel trustworthy, healthcare-oriented, and community-friendly — clean fonts, clear spacing, and strong readability from a distance.

Side One: This card has the NFC Access Card.
NEED A DOCTOR? (Large Font, Attention Grabbing)
How to Book an Appointment using your Bright Path Card
Step 1: Tap Your Card on Your Phone
Hold your card near the back of your phone.
It will activate automatically — no app needed.
The Bright Path scheduler will open.
Step 2: Schedule Your Appointment
Select your clinical concern.
Choose your time window.
Register (only once).
Confirm your appointment.
Step 3: Relax, we’ll take care of the rest
A doctor will call during your scheduled time.
Once booked, you’ll be able to call our office.
No emails, no texts — just a real person.
It’s that simple.
Side Two:
About Bright Path
Created by Dr. Marcus Ferrigan
Bright Path was founded to make healthcare simple and convenient. Prescription renewals. Common infections. Medical notes. And so much more.
Our doctors can address 120+ health concerns virtually — providing quality care without the waiting room. No waiting rooms. Just real doctors providing real care.
Why Patients Choose Bright Path
Easy access – book and be seen from anywhere in BC.
Effortless booking – tap your Bright Path Card to begin.
Trusted physicians – every visit is with a licensed BC family doctor.
How It Works
Book your visit — choose a time window that fits your day.
Join the queue — you’ll be called when it’s your turn.
Speak directly with your doctor — simple, secure, and stress-free.
Convenient Care for Common Concerns

Additional Details.
Please find the domain to be launched soon. I've attached the NFC card file for review, it is 85.5 mm x 54 mm. The card will be glued to the flyer.
I've attached examples of flyers but they are not the look I am seeking and I am looking for creative solutions.
Thank you!
http://brightpath-example.test/

Adult Patients in British Columbia

Healthcare

• Looking for clean lines, uniform appearance, and high legibility i.e poppins

0054AA
0677BA
7BADD7
CADEEF
E8F1F8

• Need A Doctor?
• Elegant style, not too busy, clear layout.
• Clutter, look cheap - review examples.

```html
<!DOCTYPE html>
<html lang="en">
<head>
<meta charset="utf-8">
<title>Bright Path Flyer – Two Sides</title>
<link href="https://fonts.googleapis.com/css2?family=Montserrat:ital,wght@0,400;0,500;0,600;0,700;0,800;1,400;1,600;1,700&family=Caveat:wght@500&display=swap" rel="stylesheet">
<style>
  :root{
    --navy:#2b418e;
    --navy-deep:#23367a;
    --sky:#1d8fd6;
    --mint:#a6d9c6;
    --mint-dark:#7fc6ab;
    --paper:#f3f3f8;
    --white:#ffffff;
    --stage:#e3e3e3;
    --ink:#2b418e;
  }
  *{box-sizing:border-box;margin:0;padding:0}
  html,body{width:1200px;height:1200px;overflow:hidden}
  body{background:var(--stage);font-family:'Montserrat',sans-serif;color:var(--ink);position:relative}
  .flyer{position:absolute;background:var(--paper);overflow:hidden}
  .flyer--front{left:130px;top:111px;width:471px;height:726px}
  .flyer--back{left:650px;top:348px;width:470px;height:725px}
  .abs{position:absolute}

  /* front */
  .hero{left:17px;top:0;width:435px;height:243px;background:var(--navy);border-radius:0 0 20px 20px;overflow:hidden}
  .hero__photo{position:absolute;right:0;top:0;width:250px;height:243px;
    background:linear-gradient(100deg,rgba(43,65,142,1) 0%,rgba(90,110,190,.75) 28%,rgba(200,215,235,.9) 60%,#e9eef5 100%)}
  .brand{display:flex;align-items:center;gap:8px;font-weight:600;white-space:nowrap}
  .brand__dot{width:12px;height:12px;border-radius:50%;background:currentColor;flex:none}
  .hero .brand{position:absolute;left:33px;top:66px;color:var(--white);font-size:30px}
  .hero__title{position:absolute;left:33px;top:140px;color:var(--white);font-weight:800;font-size:46px;line-height:43px;letter-spacing:.5px}
  .booking-intro{left:0;top:256px;width:471px;text-align:center;font-weight:600;font-size:16px;line-height:21px}
  .booking-intro em{font-weight:700}
  .step{left:38px;width:394px;background:var(--white);border-radius:12px;border-bottom:3px solid var(--navy)}
  .step::after{content:"";position:absolute;left:50%;bottom:-9px;margin-left:-7px;border:7px solid transparent;border-top-color:var(--navy);border-bottom:0}
  .step--last::after{display:none}
  .step__pill{position:absolute;left:138px;top:-13px;width:119px;height:25px;border-radius:13px;background:var(--mint);text-align:center;font-weight:700;font-size:16px;line-height:25px}
  .step__icon{position:absolute;left:20px}
  .step__body{position:absolute;left:98px;top:18px;right:8px}
  .step__title{font-weight:700;font-size:12.5px;line-height:16px;margin-bottom:3px}
  .step__list{list-style:none;font-size:9.5px;line-height:14.3px}
  .step__list li::before{content:"•";margin-right:6px;font-size:7px;vertical-align:1px}
  .tagline{left:0;top:664px;width:471px;text-align:center;font-family:'Caveat',cursive;font-size:32px}

  /* back */
  .about{left:22px;top:22px;width:427px;height:204px;background:var(--navy);border-radius:56px 56px 0 0;color:var(--white);text-align:center}
  .about__title{position:absolute;top:16px;width:100%;font-weight:700;font-size:18px;line-height:22px;letter-spacing:.3px}
  .about__swoosh{position:absolute;left:100px;top:39px}
  .about__creator{position:absolute;top:55px;width:100%;font-size:13px;line-height:26px;font-weight:700;font-style:italic}
  .about__creator span{font-family:'Caveat',cursive;font-style:normal;font-weight:500;font-size:21px;color:#37a6ef;margin-left:3px}
  .about__lead{position:absolute;top:92px;width:100%;font-size:12.5px;line-height:18px}
  .tags{position:absolute;width:100%;display:flex;justify-content:center;gap:7px}
  .tag{border:1px solid var(--white);border-radius:11px;font-size:12.5px;height:22px;line-height:20px;padding:0 10px}
  .about__more{position:absolute;top:177px;width:100%;font-style:italic;font-size:12.5px;line-height:18px}
  .promise{left:22px;top:226px;width:427px;height:113px;background:var(--white);border-radius:0 0 14px 14px;border-bottom:3px solid var(--navy);text-align:center}
  .promise__copy{position:absolute;top:13px;width:100%;font-size:13px;line-height:17px}
  .promise__strong{position:absolute;width:100%;font-weight:700;font-size:13.5px}
  .col{top:367px}
  .col--why{left:52px;width:152px}
  .col--how{left:265px;width:148px}
  .divider{left:234px;top:356px;width:1.5px;height:225px;background:var(--navy)}
  .col__title{font-weight:700;font-size:14px;line-height:17px;margin-bottom:8px}
  .feature{position:relative;padding-left:14px;margin-bottom:9px}
  .feature__check{position:absolute;left:0;top:2px}
  .feature__name{font-weight:700;font-size:11.5px;line-height:15px}
  .feature__text{font-style:italic;font-size:11.5px;line-height:15.5px}
  .back-brand{left:0;top:618px;width:470px;justify-content:center;color:var(--navy);font-size:30px}
  .band{left:0;top:671px;width:470px;height:34px;background:var(--mint);text-align:center;font-weight:700;font-style:italic;font-size:16.5px;line-height:34px}
</style>
</head>
<body>

<section class="flyer flyer--front" aria-label="Flyer side one">
  <div class="hero abs">
    <div class="hero__photo" role="img" aria-label="Photo of a doctor in a white coat holding a stethoscope, with faint medical icons"></div>
    <div class="brand"><span class="brand__dot"></span>Bright Path</div>
    <h1 class="hero__title">NEED A<br>DOCTOR?</h1>
  </div>

  <p class="booking-intro abs">How to Book an Appointment<br>using your <em>BRIGHT PATH CARD</em></p>

  <div class="step abs" style="top:325px;height:88px">
    <div class="step__pill">STEP 1</div>
    <svg class="step__icon" style="top:14px" width="42" height="58" viewBox="0 0 42 58" aria-hidden="true">
      <rect x="2" y="2" width="28" height="54" rx="4" fill="none" stroke="#2b418e" stroke-width="3"/>
      <rect x="6" y="8" width="20" height="40" fill="#fff" stroke="#2b418e" stroke-width="1.5"/>
      <rect x="12" y="51" width="8" height="2" fill="#2b418e"/>
      <path d="M31 14h7a2 2 0 0 1 2 2v26a2 2 0 0 1-2 2h-7z" fill="#2b418e"/>
    </svg>
    <div class="step__body">
      <div class="step__title">Tap Your Card on Your Phone</div>
      <ul class="step__list">
        <li>Hold your card near the back of your phone.</li>
        <li>It will activate automatically — no app needed.</li>
        <li>The Bright Path scheduler will open.</li>
      </ul>
    </div>
  </div>

  <div class="step abs" style="top:439px;height:104px">
    <div class="step__pill">STEP 2</div>
    <svg class="step__icon" style="top:33px;left:22px" width="62" height="42" viewBox="0 0 62 42" aria-hidden="true">
      <rect x="2" y="4" width="46" height="34" rx="3" fill="#fff" stroke="#2b418e" stroke-width="3"/>
      <rect x="2" y="4" width="46" height="7" fill="#2b418e"/>
      <rect x="10" y="0" width="4" height="8" rx="1" fill="#2b418e"/>
      <rect x="36" y="0" width="4" height="8" rx="1" fill="#2b418e"/>
      <g fill="#2b418e">
        <rect x="6" y="15" width="5" height="4"/><rect x="13" y="15" width="5" height="4"/><rect x="20" y="15" width="5" height="4"/><rect x="27" y="15" width="5" height="4"/><rect x="34" y="15" width="5" height="4"/><rect x="41" y="15" width="4" height="4"/>
        <rect x="6" y="22" width="5" height="4"/><rect x="13" y="22" width="5" height="4"/><rect x="20" y="22" width="5" height="4"/><rect x="27" y="22" width="5" height="4"/><rect x="34" y="22" width="5" height="4"/>
        <rect x="6" y="29" width="5" height="4"/><rect x="13" y="29" width="5" height="4"/>
      </g>
      <rect x="20" y="29" width="41" height="11" rx="4" fill="#2b418e"/>
      <text x="40.5" y="37" text-anchor="middle" font-family="Montserrat, sans-serif" font-weight="700" font-size="6.5" fill="#fff">REGISTER</text>
    </svg>
    <div class="step__body">
      <div class="step__title">Schedule Your Appointment</div>
      <ul class="step__list">
        <li>Select your clinical concern.</li>
        <li>Choose your time window.</li>
        <li>Register (only once).</li>
        <li>Confirm your appointment.</li>
      </ul>
    </div>
  </div>

  <div class="step step--last abs" style="top:570px;height:88px">
    <div class="step__pill">STEP 3</div>
    <svg class="step__icon" style="top:15px" width="54" height="58" viewBox="0 0 54 58" aria-hidden="true">
      <path d="M30 2h18a4 4 0 0 1 4 4v8a4 4 0 0 1-4 4h-10l-6 5v-5h-2a4 4 0 0 1-4-4V6a4 4 0 0 1 4-4z" fill="#fff" stroke="#2b418e" stroke-width="2"/>
      <circle cx="34" cy="10" r="1.6" fill="#2b418e"/><circle cx="39" cy="10" r="1.6" fill="#2b418e"/><circle cx="44" cy="10" r="1.6" fill="#2b418e"/>
      <circle cx="14" cy="22" r="7" fill="#2b418e"/>
      <path d="M2 52c0-10 5-16 12-16s12 6 12 16z" fill="#2b418e"/>
      <circle cx="34" cy="32" r="7" fill="#2b418e"/>
      <path d="M20 58c0-10 6-16 14-16s14 6 14 16z" fill="#2b418e"/>
    </svg>
    <div class="step__body">
      <div class="step__title">Relax, we’ll take care of the rest</div>
      <ul class="step__list">
        <li>A doctor will call during your scheduled time.</li>
        <li>Once booked, you’ll be able to call our office.</li>
        <li>No emails, no texts — just a real person.</li>
      </ul>
    </div>
  </div>

  <p class="tagline abs">It’s that simple.</p>
</section>

<section class="flyer flyer--back" aria-label="Flyer side two">
  <div class="about abs">
    <h2 class="about__title">ABOUT BRIGHT PATH</h2>
    <svg class="about__swoosh" width="80" height="8" viewBox="0 0 80 8" aria-hidden="true"><path d="M1 7C25 1 55 0 79 4" fill="none" stroke="#37a6ef" stroke-width="2"/></svg>
    <p class="about__creator">Created by<span>Dr. Marcus Ferrigan</span></p>
    <p class="about__lead">Bright Path was founded to make healthcare......</p>
    <div class="tags" style="top:118px"><span class="tag">simple and convenient</span><span class="tag">Prescription renewals</span></div>
    <div class="tags" style="top:147px"><span class="tag">Common infections</span><span class="tag">Medical notes</span></div>
    <p class="about__more">And so much more.</p>
  </div>
  <div class="promise abs">
    <p class="promise__copy">Our doctors can address 120+ health concerns virtually —<br>providing quality care without the waiting room.</p>
    <p class="promise__strong" style="top:55px">NO WAITING ROOMS.</p>
    <p class="promise__strong" style="top:79px">JUST REAL DOCTORS PROVIDING REAL CARE.</p>
  </div>

  <div class="col col--why abs">
    <h3 class="col__title">Why Patients<br>Choose Bright Path</h3>
    <div class="feature">
      <svg class="feature__check" width="10" height="10" viewBox="0 0 10 10" aria-hidden="true"><circle cx="5" cy="5" r="5" fill="#7fc6ab"/><path d="M2.5 5.2l1.7 1.6 3.3-3.4" fill="none" stroke="#fff" stroke-width="1.3"/></svg>
      <div class="feature__name">EASY ACCESS</div>
      <div class="feature__text">Book and be seen from anywhere in BC.</div>
    </div>
    <div class="feature">
      <svg class="feature__check" width="10" height="10" viewBox="0 0 10 10" aria-hidden="true"><circle cx="5" cy="5" r="5" fill="#7fc6ab"/><path d="M2.5 5.2l1.7 1.6 3.3-3.4" fill="none" stroke="#fff" stroke-width="1.3"/></svg>
      <div class="feature__name">EFFORTLESS BOOKING</div>
      <div class="feature__text">Tap your Bright Path Card to begin.</div>
    </div>
    <div class="feature">
      <svg class="feature__check" width="10" height="10" viewBox="0 0 10 10" aria-hidden="true"><circle cx="5" cy="5" r="5" fill="#7fc6ab"/><path d="M2.5 5.2l1.7 1.6 3.3-3.4" fill="none" stroke="#fff" stroke-width="1.3"/></svg>
      <div class="feature__name">TRUSTED PHYSICIANS</div>
      <div class="feature__text">Every visit is with a licensed BC family doctor.</div>
    </div>
  </div>

  <div class="divider abs"></div>

  <div class="col col--how abs">
    <h3 class="col__title">How It Works</h3>
    <div class="feature">
      <svg class="feature__check" width="10" height="10" viewBox="0 0 10 10" aria-hidden="true"><circle cx="5" cy="5" r="5" fill="#7fc6ab"/><path d="M2.5 5.2l1.7 1.6 3.3-3.4" fill="none" stroke="#fff" stroke-width="1.3"/></svg>
      <div class="feature__name">BOOK YOUR VISIT</div>
      <div class="feature__text">Choose a time window that fits your day.</div>
    </div>
    <div class="feature">
      <svg class="feature__check" width="10" height="10" viewBox="0 0 10 10" aria-hidden="true"><circle cx="5" cy="5" r="5" fill="#7fc6ab"/><path d="M2.5 5.2l1.7 1.6 3.3-3.4" fill="none" stroke="#fff" stroke-width="1.3"/></svg>
      <div class="feature__name">JOIN THE QUEUE</div>
      <div class="feature__text">You’ll be called when it’s your turn.</div>
    </div>
    <div class="feature">
      <svg class="feature__check" width="10" height="10" viewBox="0 0 10 10" aria-hidden="true"><circle cx="5" cy="5" r="5" fill="#7fc6ab"/><path d="M2.5 5.2l1.7 1.6 3.3-3.4" fill="none" stroke="#fff" stroke-width="1.3"/></svg>
      <div class="feature__name">SPEAK DIRECTLY WITH YOUR DOCTOR</div>
      <div class="feature__text">Simple, secure, and stress-free.</div>
    </div>
  </div>

  <div class="brand back-brand abs"><span class="brand__dot"></span>Bright Path</div>
  <div class="band abs">Convenient Care for Common Concerns</div>
</section>

</body>
</html>
```